Business Card Design Project

We need a double-sided business card design for our e-commerce company. Be as creative as you can.

Reason: Change of logo

Target Market(s)

Business owners

Industry/Entity Type

E-Commerce

Requirements
Must have
• Name (editable)
Mobile number -editable
www.velbiro.com - MUST STAND OUT ALONE
Office address:
27 Marlow Street
#09-04 Westbrook Tower
Singapore 048216

```html
<!DOCTYPE html>
<html lang="en">
<head>
<meta charset="utf-8">
<title>Velbiro Business Card</title>
<link rel="stylesheet" href="https://fonts.googleapis.com/css2?family=Open+Sans:wght@400;600;700&display=swap">
<style>
  :root {
    --bg: #eceff3;
    --brand-blue: #1a7fe6;
    --brand-deep: #1466c8;
    --front-light: #bfe3fb;
    --front-mid: #62b0f2;
    --front-edge: #2f8ceb;
    --ink: #1c2430;
    --ink-soft: #3a3f47;
    --divider: #8a8f96;
    --white: #ffffff;
  }
  * { box-sizing: border-box; margin: 0; padding: 0; }
  html, body { width: 1200px; height: 800px; overflow: hidden; }
  body {
    background: var(--bg);
    font-family: "Open Sans", Arial, sans-serif;
    position: relative;
  }
  .card {
    position: absolute;
    width: 560px;
    height: 320px;
    border-radius: 4px;
    box-shadow: 0 6px 18px rgba(0,0,0,0.12);
    overflow: hidden;
  }
  /* Front side */
  .card-front {
    left: 60px; top: 60px;
    background: radial-gradient(ellipse at 52% 42%, var(--front-light) 0%, var(--front-mid) 45%, var(--front-edge) 100%);
    display: flex; flex-direction: column; align-items: center; justify-content: center;
  }
  .front-brand {
    font-size: 84px; font-weight: 700; color: var(--brand-deep);
    letter-spacing: 1px; line-height: 1;
  }
  .front-tagline {
    margin-top: 22px;
    font-size: 22px; font-weight: 400; color: var(--ink);
    letter-spacing: 5px; text-transform: uppercase;
  }
  /* Back side */
  .card-back {
    left: 580px; top: 420px;
    background: var(--white);
  }
  .back-brand-block {
    position: absolute; left: 20px; top: 78px; width: 240px;
    text-align: right;
  }
  .back-brand {
    display: block; text-align: left; padding-left: 24px;
    font-size: 46px; font-weight: 700; color: var(--brand-blue); line-height: 1;
  }
  .office-address {
    margin-top: 16px; font-style: normal; white-space: nowrap;
    font-size: 11px; line-height: 1.5; color: var(--ink-soft);
  }
  .office-address strong { font-weight: 700; }
  .back-divider {
    position: absolute; left: 272px; top: 78px;
    width: 2px; height: 104px; background: var(--divider);
  }
  .person {
    position: absolute; left: 300px; top: 90px;
  }
  .person-name { font-size: 17px; font-weight: 700; color: var(--brand-blue); }
  .person-role { font-size: 12.5px; color: var(--ink-soft); margin-top: 2px; }
  .contact-list { list-style: none; margin-top: 18px; }
  .contact-list li {
    display: flex; align-items: center; gap: 8px;
    font-size: 13px; color: var(--ink-soft); margin-bottom: 8px;
  }
  .contact-list svg { width: 15px; height: 15px; flex: none; }
  .web-band { position: absolute; left: 0; bottom: 0; width: 560px; height: 66px; }
  .website {
    position: absolute; right: 40px; bottom: 14px;
    display: flex; align-items: center; gap: 8px;
    font-size: 13px; color: var(--white);
  }
  .website svg { width: 16px; height: 16px; }
</style>
</head>
<body>
  <section class="card card-front" aria-label="Card front">
    <div class="front-brand">velbiro</div>
    <p class="front-tagline">Shop Smarter Daily!</p>
  </section>

  <section class="card card-back" aria-label="Card back">
    <div class="back-brand-block">
      <span class="back-brand">velbiro</span>
      <address class="office-address">
        27 Marlow Street, #09-04 Westbrook Tower<br>
        <strong>Singapore</strong> 048216
      </address>
    </div>
    <div class="back-divider"></div>
    <div class="person">
      <p class="person-name">YOUR COMPLETE NAME</p>
      <p class="person-role">Your Position</p>
      <ul class="contact-list">
        <li>
          <svg viewBox="0 0 24 24" aria-hidden="true"><path fill="var(--brand-blue)" d="M6.6 10.8a15 15 0 0 0 6.6 6.6l2.2-2.2c.3-.3.7-.4 1-.2 1.1.4 2.3.6 3.6.6.6 0 1 .4 1 1V20c0 .6-.4 1-1 1A17 17 0 0 1 3 4c0-.6.4-1 1-1h3.5c.6 0 1 .4 1 1 0 1.3.2 2.5.6 3.6.1.3 0 .7-.2 1z"/></svg>
          123-456-7890
        </li>
        <li>
          <svg viewBox="0 0 24 24" aria-hidden="true"><path fill="none" stroke="var(--brand-blue)" stroke-width="2" d="M3 6h18v12H3z M3 6l9 7 9-7"/></svg>
          emailme@myaddress.com
        </li>
      </ul>
    </div>
    <svg class="web-band" viewBox="0 0 560 66" preserveAspectRatio="none" aria-hidden="true">
      <path fill="var(--brand-blue)" d="M0 42 L330 48 C360 48 360 22 395 22 L560 22 L560 66 L0 66 Z"/>
    </svg>
    <p class="website">
      <svg viewBox="0 0 24 24" aria-hidden="true"><g fill="none" stroke="var(--white)" stroke-width="1.6"><circle cx="12" cy="12" r="9"/><ellipse cx="12" cy="12" rx="4" ry="9"/><path d="M3 12h18M5 7h14M5 17h14"/></g></svg>
      www.velbiro.com
    </p>
  </section>
</body>
</html>
```